Business Card Design for Clinical Therapist

I will operate in 3 product areas as follows...
I will operate as Psychotherapist providing an opportunity for individuals to stop, reflect, heal, and gain hope in a safe and professional atmosphere. My task as a Licensed Mental Health Social Worker is to work “along-side” the client to help guide them toward answers they may seek. I believe that all difficulties contain a small seed of opportunity within them and I can support the individual in clarifying issues while resolving obstacles that may get in the way.
1-Therapy
Treatment Issues may include:
• Addiction
• Bipolar Disorder
• Adolescent or Adult
• Coping Skills
• Dual Diagnosis
• Family Conflict
• Sleep or Insomnia
• Substance Abuse
• Anger Management
• Career Counseling
• Drug Abuse
• Emotional Disturbance
• Grief
• Self Esteem
• Trauma and PTSD
Treatment Orientation may include but not be limited to:
• CBT
• EMDR
• Person-Centered
• Mindfulness based (MBCT)
• Motivational Interviewing

2-Other Substance Abuse Services
SAP Assessments
Employees performing safety-sensitive duties under US Bureau of Freight Conduct rules must have an evaluation by a qualified Substance Abuse Professional when they are in violation of BFC rules (for a positive test or a refusal to test). I am a BFC qualified SAP and can perform these evaluations, which involve specialized assessment and compliance reports, as well as a return to work assessment.

3-DUI/OVUII Assessments
Substance abuse assessment reports-State level assessments targeted for the court system.

Somehow I would like the final design to acknowledge the three areas of services, or two being therapy for mental health services and combining SAP/OVUII assessment reporting for Substance abuse)

Industry/Entity Type

Mental Health

Contact Information for Business Card

Brightwell Pathways LLC,
Gregory Tallmadge LCSW
Clinical Therapist
2287 East Moana Avenue, STE 412
Honolulu, HI 96822
808.541.2093
brightwellpathwaysllc.example

Colors

Designer to choose colors to be used in the design.

```html
<!DOCTYPE html>
<html lang="en">
<head>
<meta charset="utf-8">
<title>Brightwell Pathways LLC – Business Card</title>
<link rel="stylesheet" href="https://fonts.googleapis.com/css2?family=Bree+Serif&display=swap">
<style>
  :root {
    --backdrop: #e9eaeb;
    --teal-deep: #0a8fb8;
    --teal-bright: #00b0d2;
    --teal-ink: #1a8cb5;
    --paper: #ffffff;
    --band-dark: #0a7ea6;
    --band-light: #12a6cc;
  }
  * { margin: 0; padding: 0; box-sizing: border-box; }
  html, body {
    width: 1200px; height: 720px; overflow: hidden;
    background: var(--backdrop);
    font-family: "Bree Serif", Georgia, serif;
  }
  .stage { position: relative; width: 1200px; height: 720px; }
  .card {
    position: absolute; top: 241px;
    width: 420px; height: 240px; overflow: hidden;
  }
  /* Front */
  .card-front {
    left: 147px;
    background: linear-gradient(200deg, var(--teal-bright) 0%, var(--teal-deep) 100%);
  }
  .front-mark {
    position: absolute; left: -18px; top: 34px;
    width: 200px; height: 200px; border-radius: 50%;
    background: rgba(255,255,255,0.22);
  }
  .front-name {
    position: absolute; right: 22px; top: 116px;
    color: var(--paper); font-size: 15px; letter-spacing: 0.3px;
    white-space: nowrap;
  }
  /* Back */
  .card-back { left: 633px; background: var(--paper); color: var(--teal-ink); }
  .brand {
    position: absolute; left: 21px; top: 22px;
    display: flex; align-items: flex-start; gap: 12px;
  }
  .brand-dot {
    width: 32px; height: 32px; border-radius: 50%;
    background: var(--teal-ink); margin-top: 2px;
  }
  .brand-name { font-size: 15px; line-height: 18px; letter-spacing: 0.2px; }
  .brand-address { font-size: 10px; line-height: 14px; margin-top: 4px; }
  .rule {
    position: absolute; left: 21px; width: 379px; height: 1.6px;
    background: var(--teal-ink);
  }
  .rule-top { top: 126px; }
  .rule-bottom { top: 168px; }
  .person { position: absolute; left: 23px; top: 132px; }
  .person-name { font-size: 14px; line-height: 17px; }
  .person-role { font-size: 10px; line-height: 13px; }
  .contact {
    position: absolute; top: 185px; font-size: 10px; line-height: 14px;
    display: flex; align-items: center; gap: 5px;
  }
  .contact-phone { left: 23px; }
  .contact-web { right: 43px; }
  .contact svg { fill: var(--teal-ink); }
  .bottom-band {
    position: absolute; left: 0; bottom: 0; width: 100%; height: 19px;
    background: linear-gradient(90deg, var(--band-light), var(--band-dark));
  }
</style>
</head>
<body>
<main class="stage">
  <section class="card card-front" aria-label="Card front">
    <div class="front-mark" aria-hidden="true"></div>
    <p class="front-name">BRIGHTWELL PATHWAYS LLC</p>
  </section>

  <section class="card card-back" aria-label="Card back">
    <div class="brand">
      <div class="brand-dot" aria-hidden="true"></div>
      <div>
        <p class="brand-name">BRIGHTWELL PATHWAYS LLC</p>
        <p class="brand-address">2287 East Moana Avenue, STE 412 Honolulu, HI 96822</p>
      </div>
    </div>
    <div class="rule rule-top"></div>
    <div class="person">
      <p class="person-name">Gregory Tallmadge</p>
      <p class="person-role">LCSW Clinical Therapist</p>
    </div>
    <div class="rule rule-bottom"></div>
    <p class="contact contact-phone">
      <svg width="9" height="10" viewBox="0 0 24 24" aria-hidden="true"><path d="M6.6 10.8a15.1 15.1 0 0 0 6.6 6.6l2.2-2.2a1 1 0 0 1 1-.25 11.4 11.4 0 0 0 3.6.57 1 1 0 0 1 1 1V20a1 1 0 0 1-1 1A17 17 0 0 1 3 4a1 1 0 0 1 1-1h3.5a1 1 0 0 1 1 1c0 1.25.2 2.45.57 3.57a1 1 0 0 1-.25 1z"/></svg>
      808.541.2093
    </p>
    <p class="contact contact-web">
      <svg width="11" height="8" viewBox="0 0 22 16" aria-hidden="true"><path d="M0 0h22v16H0z M2 2v1l9 6 9-6V2z" fill-rule="evenodd"/></svg>
      brightwellpathwaysllc.example
    </p>
    <div class="bottom-band"></div>
  </section>
</main>
</body>
</html>
```